Wedding Day Custom Wine Label - Tasmanian (Tamar Valley) wine

I am looking for a custom design that will be put on a wine label to commemorate a very good friend's wedding day.

We will need to be able to take the design and print it on to sticker labels that we can put on to wine bottles.

The bride and groom have asked for a simplistic label design (see example image attached). We need two labels. One for "Pinot Noir" wine and the other for "Chardonnay" wine. We would like the label to say:

The Hartwell's
Pinot Noir
2023
Tamar Valley

and for for the other wine variety:

The Hartwell's
Chardonnay
2023
Tamar Valley

smaller text below to say:

13.5% ALC/VOL 750ML
MEGAN & LIAM - 31.10.2024

I am happy to consider other variations - the bride & groom would prefer something minimalistic. Elegant and classy.

Target Market(s)

the bride & groom

Requirements
Must have
• Wedding date (31.10.2024). Wine type (Pinot Noir or Chardonnay).
Should not have
• images not essential

```html
<!DOCTYPE html>
<html lang="en">
<head>
<meta charset="utf-8">
<title>The Hartwell's Wedding Wine Label</title>
<link href="https://fonts.googleapis.com/css2?family=Playfair+Display:ital,wght@1,400&family=Montserrat:wght@300;400&display=swap" rel="stylesheet">
<style>
  :root {
    --navy-core: #25215a;
    --navy-edge: #19182f;
    --gold-line: #c9a14f;
    --gold-ornament: #b8924a;
    --sand: #d2bd9e;
    --amber: #d29036;
  }
  * { margin: 0; padding: 0; box-sizing: border-box; }
  html, body { width: 922px; height: 1200px; overflow: hidden; }
  body { background: var(--navy-edge); }
  .label {
    position: relative;
    width: 922px;
    height: 1200px;
    overflow: hidden;
    background: radial-gradient(ellipse 60% 50% at 50% 45%, var(--navy-core) 0%, #211f4c 55%, var(--navy-edge) 100%);
  }
  .label__frame { position: absolute; inset: 0; }
  .ornament {
    position: absolute;
    background: radial-gradient(circle, rgba(184,146,74,0.45) 0%, rgba(184,146,74,0.12) 60%, rgba(184,146,74,0) 100%);
    border-radius: 50%;
  }
  .ornament--corner { width: 140px; height: 140px; }
  .ornament--tl { left: 25px; top: 25px; }
  .ornament--tr { right: 25px; top: 25px; }
  .ornament--bl { left: 25px; bottom: 25px; }
  .ornament--br { right: 25px; bottom: 25px; }
  .ornament--crown { left: 285px; top: 0; width: 50px; height: 22px; }
  .ornament--fleuron-top { left: 422px; top: 182px; width: 110px; height: 80px; background: radial-gradient(ellipse, rgba(201,161,79,0.75) 0%, rgba(201,161,79,0.2) 60%, rgba(201,161,79,0) 100%); }
  .ornament--fleuron-bottom { left: 422px; top: 1025px; width: 110px; height: 70px; background: radial-gradient(ellipse, rgba(201,161,79,0.75) 0%, rgba(201,161,79,0.2) 60%, rgba(201,161,79,0) 100%); }

  .label__title {
    position: absolute;
    left: 0; right: 0;
    top: 270px;
    text-align: center;
    font-family: "Playfair Display", serif;
    font-style: italic;
    font-weight: 400;
    color: var(--sand);
    line-height: 1;
  }
  .label__title-article { display: block; font-size: 88px; margin-left: -40px; }
  .label__title-name { display: block; font-size: 132px; margin-top: -22px; letter-spacing: -1px; }

  .label__variety, .label__region, .label__vintage, .label__details, .label__dedication {
    position: absolute; left: 0; right: 0; text-align: center;
    font-family: "Montserrat", sans-serif;
    font-weight: 400;
    line-height: 1.2;
  }
  .label__variety {
    top: 572px; font-size: 74px;
    letter-spacing: 0.27em; padding-left: 0.27em; color: var(--amber);
  }
  /* Variety switch: set .label--chardonnay or .label--pinot-noir on the label */
  .label--chardonnay .variety--pinot-noir,
  .label--pinot-noir .variety--chardonnay { display: none; }

  .label__region {
    top: 668px; font-size: 64px;
    letter-spacing: 0.16em; color: var(--sand); padding-left: 40px;
  }
  .label__region-dot { margin-left: 22px; }
  .label__vintage {
    top: 758px; font-size: 58px;
    letter-spacing: 0.32em; padding-left: 0.32em; color: var(--amber);
  }
  .label__details {
    top: 896px; font-size: 31px; color: var(--sand);
  }
  .label__dedication {
    top: 940px; font-size: 40px; color: var(--sand);
  }
</style>
</head>
<body>
<main class="label label--chardonnay">
  <svg class="label__frame" width="922" height="1200" viewBox="0 0 922 1200" aria-hidden="true">
    <path d="M80 178 H160 C215 178 230 40 461 33 C692 40 710 178 765 178 H845 Q880 178 880 213 V965 Q880 1000 845 1000 H760 C705 1000 690 1165 461 1170 C232 1165 217 1000 162 1000 H77 Q42 1000 42 965 V213 Q42 178 77 178 Z"
          fill="none" stroke="var(--gold-line)" stroke-width="4"/>
  </svg>

  <div class="ornament ornament--corner ornament--tl" role="img" aria-label="Gold filigree corner flourish"></div>
  <div class="ornament ornament--corner ornament--tr" role="img" aria-label="Gold filigree corner flourish"></div>
  <div class="ornament ornament--corner ornament--bl" role="img" aria-label="Gold filigree corner flourish"></div>
  <div class="ornament ornament--corner ornament--br" role="img" aria-label="Gold filigree corner flourish"></div>
  <div class="ornament ornament--crown" role="img" aria-label="Small gold scroll flourish at the top edge"></div>
  <div class="ornament ornament--fleuron-top" role="img" aria-label="Gold fleuron ornament"></div>
  <div class="ornament ornament--fleuron-bottom" role="img" aria-label="Gold fleuron ornament"></div>

  <h1 class="label__title">
    <span class="label__title-article">The</span>
    <span class="label__title-name">Hartwell's</span>
  </h1>

  <p class="label__variety"><span class="variety variety--chardonnay">CHARDONNAY</span><span class="variety variety--pinot-noir">PINOT NOIR</span></p>
  <p class="label__region">Tamar Valley<span class="label__region-dot">·</span></p>
  <p class="label__vintage">2023</p>
  <p class="label__details">13.5% ALC/VOL 750ML</p>
  <p class="label__dedication">MEGAN &amp; LIAM - 31.10.2024</p>
</main>
</body>
</html>
```